Developer needs a Software blog Design

I need a design for my software blog (I'm a developer). The design should include a homepage for browser and for mobile.

Following is a wireframe: https://sketchgrid.example/kQp7wz.

The sidebar can also include my picture I you think it should.

In the mobile version the about me and subscribe with email should be popup or dropdown.

I'm currently using this: http://tavelkin.inkpage.example/ which I like, but doesn't have all the component I want on the sidebar and I want something unique.

The most importnant is simple, clean and responsive.

Designs that I like:
http://blog.rupolat.example/
http://xwrt.example/layoutbazaar/?theme=fens
http://demo.skinorbit.example/#singularly

Out come should be a psd file with homepage and mobile homepage (and dropdowns variation for the mobile).

Target Market(s)

developers

Industry/Entity Type

Software

Font styles to use
Sans Serif

Requirements
Must have
• clean and simple. responsive. main post area need to be wide enough.

```html
<!DOCTYPE html>
<html lang="en">
<head>
<meta charset="utf-8">
<title>Tavelkin — Software Blog</title>
<link href="https://fonts.googleapis.com/css2?family=Open+Sans:wght@400;600&family=Noto+Sans:wght@400&display=swap" rel="stylesheet">
<style>
:root{
  --teal:#23b4ac;
  --teal-dark:#1d9d96;
  --side:#2e2f37;
  --side-top:#25262d;
  --side-foot:#222329;
  --side-text:#d7d8dc;
  --side-line:#3d3e47;
  --orange:#f47b10;
  --page:#f6f6f6;
  --ink:#3a3a3a;
  --muted:#666;
  --rule:#e3e3e3;
  --chirper:#3a8fd9;
  --facepage:#3c5c99;
}
*{box-sizing:border-box;margin:0;padding:0}
html,body{width:911px;height:1200px;overflow:hidden}
body{position:relative;background:var(--page);font-family:"Open Sans",sans-serif;color:var(--ink)}
.abs{position:absolute}

/* sidebar */
.sidebar{position:absolute;left:0;top:0;width:254px;height:1200px;background:var(--side);color:var(--side-text)}
.brand-bar{position:absolute;left:0;top:0;width:254px;height:92px;background:var(--side-top)}
.brand{position:absolute;left:0;top:12px;width:254px;text-align:center;font-size:21px;font-weight:600;letter-spacing:.5px;color:var(--teal)}
.avatar{position:absolute;left:72px;top:50px;width:108px;height:108px;border-radius:50%;border:4px solid #fff;background:linear-gradient(160deg,#8e9aa3,#3e4348);box-shadow:0 0 0 3px #24252b}
.search-band{position:absolute;left:0;top:175px;width:254px;height:55px;background:var(--teal)}
.search{position:absolute;left:21px;top:11px;width:212px;height:31px;background:#fff;border-radius:3px;font-size:10px;color:#777;padding:9px 10px}
.search svg{position:absolute;right:11px;top:10px}
.cta-label{position:absolute;left:20px;top:244px;font-size:9.5px;color:#fff;letter-spacing:.1px}
.field{position:absolute;left:21px;top:271px;width:208px;height:39px;border:1px solid var(--side-line);font-size:9.5px;color:#8a8b92;padding:13px 12px}
.btn-outline{position:absolute;left:20px;top:322px;width:77px;height:28px;border:1px solid var(--side-line);font-size:10px;color:#8a8b92;text-align:center;line-height:26px}
.btn-solid{position:absolute;left:21px;width:211px;height:38px;border-radius:2px;color:#fff;font-size:12px;display:flex;align-items:center;justify-content:center;gap:9px}
.btn-rss{top:373px;background:var(--orange)}
.btn-mail{top:422px;background:var(--teal)}
.side-heading{position:absolute;left:20px;font-family:"Noto Sans",sans-serif;color:#fff}
.recent-heading{top:488px;font-size:14.5px}
.recent-rule{position:absolute;left:21px;top:519px;width:211px;height:1px;background:#5a5b64}
.recent-rule::before{content:"";position:absolute;left:0;top:0;width:90px;height:1px;background:var(--teal)}
.recent{position:absolute;left:22px;width:214px;height:70px}
.recent .thumb{position:absolute;left:0;top:0;width:74px;height:64px}
.recent h4{position:absolute;left:88px;top:-2px;font-family:"Noto Sans",sans-serif;font-weight:400;font-size:11.5px;color:#fff}
.recent p{position:absolute;left:89px;top:18px;width:130px;font-size:9px;line-height:16.8px;color:var(--side-text)}
.about-heading{top:790px;font-size:18px}
.about-text{position:absolute;left:21px;top:820px;width:222px;font-size:9.5px;line-height:18.4px;color:var(--side-text)}
.social{position:absolute;left:22px;top:909px;display:flex;gap:2px}
.social span{width:37px;height:29px;background:var(--teal);display:flex;align-items:center;justify-content:center}
.side-foot{position:absolute;left:0;top:1152px;width:254px;height:48px;background:var(--side-foot);font-size:9.5px;color:#e6e6e6;padding:17px 19px}

/* main */
.topnav{position:absolute;left:254px;top:0;width:657px;height:42px;background:var(--teal);font-size:13px;color:#fff}
.topnav a{position:absolute;top:12px;color:#fff;text-decoration:none}
.hero{position:absolute;left:274px;top:62px;width:616px;height:265px;background:linear-gradient(120deg,#e6e8ea 0%,#cfd3d6 50%,#9d8a7e 78%,#c9ccce 100%)}
.hero-caption{position:absolute;left:0;bottom:0;width:100%;height:47px;background:rgba(70,72,78,.85);color:#eee;font-size:14.5px;padding:13px 23px}
.hero-caption svg{position:absolute;right:20px;top:17px}
.post-title{position:absolute;left:274px;font-family:"Noto Sans",sans-serif;font-weight:400;font-size:24px;color:#333}
.meta{position:absolute;left:274px;font-size:9.5px;color:#444;display:flex;align-items:center;gap:5px}
.meta .tag{margin-left:18px;display:flex;align-items:center;gap:5px}
.rule{position:absolute;left:274px;width:616px;height:1px;background:var(--rule)}
.lead{position:absolute;left:277px;font-size:13px;color:#444}
.body{position:absolute;left:274px;width:616px;font-size:8.9px;line-height:18.4px;color:var(--muted)}
.share{position:absolute;top:554px;height:32px;border-radius:3px;color:#fff;font-size:10.5px;font-weight:600;display:flex;align-items:center;justify-content:center;gap:7px;border-bottom:2px solid rgba(0,0,0,.15)}
.share i{width:8px;height:8px;border-radius:50%;background:#fff;display:block}
.share-chirper{left:274px;width:100px;background:var(--chirper)}
.share-facepage{left:385px;width:100px;background:var(--facepage)}
.share-circle{left:500px;width:121px;background:var(--teal)}
.comments-heading{position:absolute;left:275px;top:614px;font-family:"Noto Sans",sans-serif;font-size:19.5px;color:#333}
.comment{position:absolute;left:277px;width:612px;height:60px}
.comment .face{position:absolute;left:0;top:0;width:57px;height:50px;border:1px solid #ddd;padding:2px;background:#fff}
.comment .face div{width:100%;height:100%;background:linear-gradient(180deg,#c9ced3,#6f7479)}
.comment h5{position:absolute;left:68px;top:-3px;font-family:"Noto Sans",sans-serif;font-weight:400;font-size:12.5px;color:#444}
.comment p{position:absolute;left:68px;top:17px;width:540px;font-size:9px;line-height:17px;color:#444}
.comment p b{font-weight:400;color:#111}
</style>
</head>
<body>

<aside class="sidebar">
  <div class="brand-bar"></div>
  <div class="brand">TAVELKIN</div>
  <div class="avatar" role="img" aria-label="Portrait photo of the blog author"></div>

  <div class="search-band">
    <div class="search">search
      <svg width="10" height="10" viewBox="0 0 10 10"><circle cx="4" cy="4" r="3" fill="none" stroke="#555" stroke-width="1.4"/><line x1="6.2" y1="6.2" x2="9" y2="9" stroke="#555" stroke-width="1.4"/></svg>
    </div>
  </div>

  <div class="cta-label">CALL FOR ACTION FOR SUSCRIBE TO EMAIL</div>
  <div class="field">E - MAIL</div>
  <div class="btn-outline">SUSCRIBE</div>

  <div class="btn-solid btn-rss">
    <svg width="15" height="15" viewBox="0 0 15 15"><circle cx="2.5" cy="12.5" r="2" fill="#fff"/><path d="M1 6a8 8 0 0 1 8 8" fill="none" stroke="#fff" stroke-width="2.2"/><path d="M1 1a13 13 0 0 1 13 13" fill="none" stroke="#fff" stroke-width="2.2"/></svg>
    SUBSCRIBE VIA RSS
  </div>
  <div class="btn-solid btn-mail">
    <svg width="15" height="11" viewBox="0 0 15 11"><rect x="1" y="1" width="13" height="9" rx="1" fill="none" stroke="#fff" stroke-width="1.5"/><path d="M1 1.5l6.5 5 6.5-5" fill="none" stroke="#fff" stroke-width="1.5"/></svg>
    SUBSCRIBE VIA EMAIL
  </div>

  <h3 class="side-heading recent-heading">Recent Posts</h3>
  <div class="recent-rule"></div>

  <div class="recent" style="top:538px">
    <div class="thumb" role="img" aria-label="Businessman on a rooftop overlooking a city" style="background:linear-gradient(180deg,#c7d3de,#6d7480)"></div>
    <h4>Token-Based PubSub</h4>
    <p>Lorem ipsum dolor sit amet, consectetur adipiscing elit, sed do eiusmod tempor</p>
  </div>
  <div class="recent" style="top:622px">
    <div class="thumb" role="img" aria-label="Person in a suit touching a gear graphic" style="background:linear-gradient(160deg,#5d6169,#2a2c31)"></div>
    <h4>Token-Based PubSub</h4>
    <p>Lorem ipsum dolor sit amet, consectetur adipiscing elit, sed do eiusmod tempor</p>
  </div>
  <div class="recent" style="top:706px">
    <div class="thumb" role="img" aria-label="Hands signing paperwork at a desk" style="background:linear-gradient(160deg,#dfe6ee,#9fb0c2)"></div>
    <h4>Token-Based PubSub</h4>
    <p>Lorem ipsum dolor sit amet, consectetur adipiscing elit, sed do eiusmod tempor</p>
  </div>

  <h3 class="side-heading about-heading">About Me</h3>
  <p class="about-text">Lorem ipsum dolor sit amet, consectetur adipiscing elit, sed do eiusmod tempor incididunt ut labore et dolore magna aliqua. Ut enim ad minim veniam, quis nostrud exercitation ullamco</p>

  <div class="social">
    <span><svg width="17" height="17"><circle cx="8.5" cy="8.5" r="7.5" fill="none" stroke="#fff" stroke-width="1.3"/></svg></span>
    <span><svg width="17" height="17"><circle cx="8.5" cy="8.5" r="7.5" fill="none" stroke="#fff" stroke-width="1.3"/></svg></span>
    <span><svg width="17" height="17" viewBox="0 0 17 17"><circle cx="8.5" cy="8.5" r="7.5" fill="none" stroke="#fff" stroke-width="1.3"/><rect x="4.5" y="6" width="8" height="5.5" fill="none" stroke="#fff" stroke-width="1.1"/><path d="M4.5 6l4 3 4-3" fill="none" stroke="#fff" stroke-width="1.1"/></svg></span>
    <span><svg width="17" height="17"><circle cx="8.5" cy="8.5" r="7.5" fill="none" stroke="#fff" stroke-width="1.3"/></svg></span>
  </div>

  <div class="side-foot">Copyright © 2014 Tavelkin . All rights reserved.</div>
</aside>

<nav class="topnav">
  <a style="left:59px">All Blogs</a>
  <a style="left:152px">Most Recent</a>
  <a style="left:268px">Most Popular</a>
  <a style="left:387px">Featured Blogs</a>
</nav>

<main>
  <div class="hero" role="img" aria-label="Hand holding a smartphone sending a document to a printer">
    <div class="hero-caption">Sed ut perspiciatis unde omnis iste natus error sit
      <svg width="26" height="12" viewBox="0 0 26 12"><path d="M6 1L1 6l5 5M20 1l5 5-5 5" fill="none" stroke="#fff" stroke-width="1.6"/></svg>
    </div>
  </div>

  <h1 class="post-title" style="top:346px">Token-Based PubSub</h1>
  <div class="meta" style="top:389px">
    <svg width="9" height="9"><rect x=".5" y="1.5" width="8" height="7" fill="none" stroke="#23b4ac"/><rect x=".5" y="1.5" width="8" height="2" fill="#23b4ac"/></svg>19 days ago
    <span class="tag"><svg width="9" height="9"><path d="M0 0h5l4 4-5 5-4-4z" fill="#23b4ac"/></svg>NetQL · PubSub</span>
  </div>
  <div class="rule" style="top:417px"></div>
  <p class="lead" style="top:432px">I recently pushed two new features to both QueueLite and NetQL</p>
  <p class="body" style="top:465px">manual subscriptions and welcome message, both for the XFan socket. In this post, I will explore what we can do with the manual subscrip-tions feature. The next post will cover the welcome message. Neither feature is part of any release of QueueLite or NetQL yet, so you will have to compile from the source code to use the new features. I will use NetQL throughout the post, but you can implement the examples using any QueueLite binding.</p>

  <div class="share share-chirper"><i></i>CHIRPER</div>
  <div class="share share-facepage"><i></i>FACEPAGE</div>
  <div class="share share-circle"><i></i>CIRCLE PLUS</div>

  <h2 class="comments-heading">Comments (15)</h2>
  <div class="rule" style="top:654px"></div>

  <div class="comment" style="top:678px"><div class="face"><div role="img" aria-label="Commenter portrait"></div></div><h5>Maren Okoli</h5><p>Nemo enim ipsam voluptatem quia voluptas sit as &nbsp;sed <b>http://tavelkin.inkpage.example</b> &nbsp;quia consequuntur magni dolores quia consequuntur magni dolores &nbsp;quia consequuntur magni dolores</p></div>
  <div class="comment" style="top:742px"><div class="face"><div role="img" aria-label="Commenter portrait"></div></div><h5>Maren Okoli</h5><p>Nemo enim ipsam voluptatem quia voluptas sit as &nbsp;sed <b>http://tavelkin.inkpage.example</b> &nbsp;quia consequuntur magni dolores quia consequuntur magni dolores &nbsp;quia consequuntur magni dolores</p></div>
  <div class="comment" style="top:805px"><div class="face"><div role="img" aria-label="Commenter portrait"></div></div><h5>Maren Okoli</h5><p>Nemo enim ipsam voluptatem quia voluptas sit as &nbsp;sed <b>http://tavelkin.inkpage.example</b> &nbsp;quia consequuntur magni dolores quia consequuntur magni dolores &nbsp;quia consequuntur magni dolores</p></div>
  <div class="comment" style="top:869px"><div class="face"><div role="img" aria-label="Commenter portrait"></div></div><h5>Maren Okoli</h5><p>Nemo enim ipsam voluptatem quia voluptas sit as &nbsp;sed <b>http://tavelkin.inkpage.example</b> &nbsp;quia consequuntur magni dolores quia consequuntur magni dolores &nbsp;quia consequuntur magni dolores</p></div>
  <div class="comment" style="top:932px"><div class="face"><div role="img" aria-label="Commenter portrait"></div></div><h5>Maren Okoli</h5><p>Nemo enim ipsam voluptatem quia voluptas sit as &nbsp;sed <b>http://tavelkin.inkpage.example</b> &nbsp;quia consequuntur magni dolores quia consequuntur magni dolores &nbsp;quia consequuntur magni dolores</p></div>

  <h1 class="post-title" style="top:1010px">Permission-Based PubSub</h1>
  <div class="meta" style="top:1053px">
    <svg width="9" height="9"><rect x=".5" y="1.5" width="8" height="7" fill="none" stroke="#23b4ac"/><rect x=".5" y="1.5" width="8" height="2" fill="#23b4ac"/></svg>19 days ago
    <span class="tag"><svg width="9" height="9"><path d="M0 0h5l4 4-5 5-4-4z" fill="#23b4ac"/></svg>NetQL · PubSub</span>
  </div>
  <div class="rule" style="top:1081px"></div>
  <p class="lead" style="top:1095px">I recently pushed two new features to both QueueLite and NetQL</p>
  <p class="body" style="top:1128px">manual subscriptions and welcome message, both for the XFan socket. In this post, I will explore what we can do with the manual subscrip-tions feature. The next post will cover the welcome message. Neither feature is part of any release of QueueLite or NetQL yet, so you will have to compile from the source code to use the new features. I will use NetQL throughout the post, but you can</p>
</main>

</body>
</html>
```